Certified Probate & Trust Postcard

Hi, I am looking for your assistance. I need a postcard design based on the following specifications. The postcard needs to be 6x9. Here are the specifications for the front and back sides. I also need help incorporating a section on the front of the postcard where I can write the name or names of the people I am addressing the postcard to, as well as a space on the back for the stamp and the receiver's address.

(revised 6/18/2025)
🖼️ FRONT SIDE

(Visual: A serene Bay Area home or warm, sunlit interior. Include Tessa’s headshot. Color palette: ivory, slate, soft gold.)

Headline:

You’ve Taken On So Much — Let Me Help with What Comes Next

Subhead:

Strategic Real Estate Guidance for Probate & Trust
Certified Probate & Trust Specialist | Serving the San Francisco Bay Area

⸻

đź“© BACK SIDE

Opening Quote (italicized):

“I lost both of my parents in 2020 — just weeks apart. That experience shaped how I serve every estate I touch.”

⸻

Main Body Copy:

My name is Tessa Harlow, and I’m a Certified Probate & Trust Specialist who works with families, attorneys, and fiduciaries to guide the real estate side of probate with structure, sensitivity, and strategy.

Whether you’re navigating this with legal support or filing in pro per, this process is layered — emotional, procedural, and often overwhelming. I provide a steady hand when everything else feels uncertain.

With over a decade of experience supporting executives at Corvana, Lumidel, and Dunmore Kass, I bring the same operational precision and discretion to every estate I manage. But I also bring empathy — because I’ve been in your shoes.

⸻

What I Offer — At No Upfront Cost to the Estate:
• Property clean-outs, inspections, and basic preparation — coordinated and covered
• Real estate strategy aligned with court timelines and estate goals
• Hands-on collaboration with attorneys or step-by-step guidance for independent petitioners
• Thoughtful communication that honors your time and your grief

Because real estate isn’t just business.
For you, it’s personal. For me, it’s both.

⸻

Call to Action (in soft gold frame or slate border):

If you’re managing a probate or trust estate and need support you can trust — let’s make this easier, together.
Snapgram: @itstessavoy | CareerNet: profilehub.example/in/tessahomeguide

Industry/Entity Type

Real Estate

Requirements
Must have
• Image needs to have a calm aesthetic (remember the person receiving is grieving) emphasis on luxury as we are looking to attract high end clients so not generic and something that is easily purchased from craftly
Nice to have
• need the following design scheme as it relates to color and font Primary Color Palette: 1. Ecru Stone (Soft Beige/Taupe) – #D7CCC0 • Evokes warmth, trust, and sophistication. 2. Slate Charcoal (Deep Neutral Gray) – #4A4A4A • Represents professionalism, authority, and reliability. Accent Colors: 3. Soft Gold (Understated Elegance) – #C2B280 • Adds a subtle richness without being flashy. 4. Powder White (Clean Background Base) – #FAF9F6 • Used for breathing room, high readability, and elegance. Typography/Callout Highlight Color: 5. Trust Blue (Soft Navy) – #3F4A5F • Often used for headers or key points to add credibility and depth. Tessa Harlow should be in cursive, readable and absolutely beautiful
Should not have
• No yellow, do not use ai on my image,

```html
<!DOCTYPE html>
<html lang="en">
<head>
<meta charset="UTF-8">
<title>Certified Probate &amp; Trust Postcard</title>
<link rel="stylesheet" href="https://fonts.googleapis.com/css2?family=Poiret+One&family=Poppins:wght@300;400&family=Sacramento&display=swap">
<style>
  :root {
    --ecru-stone: #D7CCC0;
    --slate-charcoal: #4A4A4A;
    --soft-gold: #C2B280;
    --powder-white: #FAF9F6;
    --trust-blue: #3F4A5F;
    --ink: #3b3b3b;
    --frame: #555555;
    --warm-light: #efe6da;
    --sand: #e4d6c4;
    --mist: #cdd3d8;
  }
  * { margin: 0; padding: 0; box-sizing: border-box; }
  html, body { width: 879px; height: 1200px; overflow: hidden; background: #ffffff; }
  body { position: relative; font-family: "Poppins", sans-serif; color: var(--ink); }

  .postcard {
    position: absolute;
    left: 69px;
    width: 751px;
    height: 500px;
    border: 1px solid var(--frame);
    overflow: hidden;
    background: #ffffff;
  }
  .postcard--front { top: 68px; }
  .postcard--back { top: 602px; }

  /* FRONT */
  .interior-photo {
    position: absolute;
    left: 26px; top: 0;
    width: 725px; height: 400px;
    background:
      linear-gradient(90deg, rgba(255,255,255,0.95) 0%, rgba(255,255,255,0.35) 18%, rgba(255,255,255,0) 40%),
      linear-gradient(180deg, #e2d3bf 0%, #efe5d7 30%, #f4ede3 55%, #e9dccb 80%, #ddd0bf 100%);
  }
  .lower-fade {
    position: absolute;
    left: 26px; top: 459px;
    width: 725px; height: 41px;
    background: linear-gradient(90deg, #f7f7f7 0%, #dfe3e6 40%, #c9ced2 80%, #e6e8ea 100%);
  }
  .headline {
    position: absolute;
    left: 47px; top: 86px;
    font-family: "Poiret One", sans-serif;
    font-size: 53px;
    line-height: 66px;
    font-weight: 400;
    color: var(--slate-charcoal);
    letter-spacing: -0.5px;
  }
  .title-band {
    position: absolute;
    left: 26px; top: 400px;
    width: 725px; height: 59px;
    background: #ffffff;
  }
  .subhead {
    position: absolute;
    left: 40px; top: 10px;
    font-size: 16.5px;
    font-weight: 400;
    letter-spacing: 0.2px;
    color: var(--slate-charcoal);
  }
  .subline {
    position: absolute;
    left: 40px; top: 32px;
    font-size: 12.5px;
    font-weight: 300;
    letter-spacing: 0.3px;
    color: #555;
  }
  .headshot {
    position: absolute;
    left: 540px; top: 284px;
    width: 176px; height: 176px;
    border-radius: 50%;
    border: 5px solid var(--ecru-stone);
    background: radial-gradient(circle at 50% 40%, #a57d66 0%, #6b4a3b 35%, #2d2523 65%, #f1ede9 66%);
  }

  /* BACK */
  .back-glow {
    position: absolute;
    left: 0; top: 0;
    width: 751px; height: 268px;
    background: radial-gradient(ellipse 420px 260px at 0% 0%, var(--sand) 0%, #efe7dd 45%, rgba(255,255,255,0) 100%);
  }
  .opening-quote {
    position: absolute;
    left: 26px; top: 18px;
    font-family: "Sacramento", cursive;
    font-size: 26px;
    line-height: 32px;
    color: var(--slate-charcoal);
  }
  .story {
    position: absolute;
    left: 26px; top: 102px;
    width: 440px;
    font-size: 10.6px;
    line-height: 12.6px;
    color: #222;
  }
  .story p { margin-bottom: 12.5px; }
  .stamp-box {
    position: absolute;
    left: 648px; top: 20px;
    width: 76px; height: 76px;
    border: 1.2px solid var(--frame);
    border-radius: 7px;
  }
  .address-line {
    position: absolute;
    left: 487px;
    width: 237px;
    height: 0;
    border-top: 1px solid var(--frame);
  }
  .address-line--one { top: 152px; }
  .address-line--two { top: 201px; }

  .offer-band {
    position: absolute;
    left: 0; top: 268px;
    width: 751px; height: 153px;
    background: var(--ecru-stone);
  }
  .offer-frame {
    position: absolute;
    left: 25px; top: 26px;
    width: 698px; height: 103px;
    border: 1px solid var(--frame);
    border-top: none;
  }
  .offer-frame::before, .offer-frame::after {
    content: "";
    position: absolute;
    top: 0;
    border-top: 1px solid var(--frame);
  }
  .offer-frame::before { left: 0; width: 96px; }
  .offer-frame::after { right: 0; width: 94px; }
  .offer-title {
    position: absolute;
    left: 0; top: -10px;
    width: 100%;
    text-align: center;
    font-size: 16.5px;
    font-weight: 400;
    color: var(--slate-charcoal);
    letter-spacing: 0.2px;
    line-height: 20px;
  }
  .offer-list {
    position: absolute;
    list-style: none;
    font-size: 12px;
    line-height: 14px;
    color: #222;
  }
  .offer-list li { margin-bottom: 14px; }
  .offer-list--left { left: 24px; top: 19px; width: 300px; }
  .offer-list--right { left: 346px; top: 19px; width: 335px; }

  .contact-bar {
    position: absolute;
    left: 0; top: 421px;
    width: 751px; height: 45px;
    background: var(--slate-charcoal);
    color: #ffffff;
    text-align: center;
  }
  .contact-invite { font-size: 11.4px; line-height: 13px; padding-top: 8px; font-weight: 300; }
  .contact-handles { font-size: 14px; line-height: 18px; font-weight: 300; letter-spacing: 0.2px; }
  .closing-line {
    position: absolute;
    left: 0; top: 472px;
    width: 751px;
    text-align: center;
    font-size: 15px;
    color: var(--slate-charcoal);
    letter-spacing: 0.2px;
  }
</style>
</head>
<body>

<section class="postcard postcard--front">
  <div class="interior-photo" role="img" aria-label="Sunlit, calm ivory and warm-wood living room with a coastal view"></div>
  <div class="lower-fade"></div>
  <h1 class="headline">You’ve Taken On<br>So Much —<br>Let Me Help with<br>What Comes Next</h1>
  <div class="title-band">
    <p class="subhead">STRATEGIC REAL ESTATE GUIDANCE FOR PROBATE &amp; TRUST</p>
    <p class="subline">Certified Probate &amp; Trust Specialist | Serving the San Francisco Bay Area</p>
  </div>
  <div class="headshot" role="img" aria-label="Headshot of Tessa Harlow"></div>
</section>

<section class="postcard postcard--back">
  <div class="back-glow"></div>
  <blockquote class="opening-quote">“I lost both of my parents in 2020 — just weeks apart.<br>That experience shaped how I serve every estate I touch.”</blockquote>
  <div class="story">
    <p>My name is Tessa Harlow, and I’m a Certified Probate &amp; Trust Specialist who works with families, attorneys, and fiduciaries to guide the real estate side of probate with structure, sensitivity, and strategy.</p>
    <p>Whether you’re navigating this with legal support or filing in pro per, this process is layered — emotional, procedural, and often overwhelming. I provide a steady hand when everything else feels uncertain.</p>
    <p>With over a decade of experience supporting executives at Corvana, Lumidel, and Dunmore Kass, I bring the same operational precision and discretion to every estate I manage. But I also bring empathy — because I’ve been in your shoes.</p>
  </div>
  <div class="stamp-box"></div>
  <div class="address-line address-line--one"></div>
  <div class="address-line address-line--two"></div>

  <div class="offer-band">
    <div class="offer-frame">
      <h2 class="offer-title">WHAT I OFFER — AT NO UPFRONT COST TO THE ESTATE:</h2>
      <ul class="offer-list offer-list--left">
        <li>• Property clean-outs, inspections, and basic preparation — coordinated and covered.</li>
        <li>• Real estate strategy aligned with court timelines and estate goals.</li>
      </ul>
      <ul class="offer-list offer-list--right">
        <li>• Hands-on collaboration with attorneys or Step-by-step guidance for independent petitioners.</li>
        <li>• Thoughtful communication that honors your time and your grief.</li>
      </ul>
    </div>
  </div>

  <div class="contact-bar">
    <p class="contact-invite">If you’re managing a probate or trust estate and need support you can trust — let’s make this easier, together.</p>
    <p class="contact-handles">Snapgram: @itstessavoy | CareerNet: profilehub.example/in/tessahomeguide</p>
  </div>
  <p class="closing-line">BECAUSE REAL ESTATE ISN’T JUST BUSINESS. FOR YOU, IT’S PERSONAL. FOR ME, IT’S BOTH.</p>
</section>

</body>
</html>
```